November Online Auction

November Online Farm and Construction Machinery Auction November 4th Thru The 7th Now Accepting Farm and Construction related Items Till November 1 St

```html
<!DOCTYPE html>
<html lang="en">
<head>
<meta charset="utf-8">
<title>November Online Auction – Postcard</title>
<link href="https://fonts.googleapis.com/css2?family=Bebas+Neue&family=Montserrat:wght@400;600;700;800&display=swap" rel="stylesheet">
<style>
  :root{
    --orange:#f0962a;
    --dark:#262626;
    --white:#ffffff;
    --paper:#f7f7f7;
    --stage:#e6e6e6;
    --line:#cfcfcf;
    --head:'Bebas Neue', Impact, sans-serif;
    --body:'Montserrat', Arial, sans-serif;
  }
  *{box-sizing:border-box;margin:0;padding:0}
  html,body{width:1200px;height:900px;overflow:hidden}
  body{background:var(--stage);position:relative;font-family:var(--body)}
  .postcard{position:absolute;top:260px;width:570px;height:380px;background:var(--paper);overflow:hidden;box-shadow:0 6px 18px rgba(0,0,0,.18)}
  .postcard--front{left:20px}
  .postcard--back{left:610px}
  .postcard__shapes{position:absolute;inset:0}
  .abs{position:absolute}

  .brand{display:flex;align-items:center;gap:6px;white-space:nowrap}
  .brand__dot{width:26px;height:26px;border-radius:50%;background:var(--orange);flex:none}
  .brand__name{font-family:var(--head);color:var(--orange);font-size:22px;line-height:.9;letter-spacing:.5px}

  .headline{font-family:var(--head);color:var(--white);line-height:.92;letter-spacing:.3px}
  .headline__dark{color:var(--dark)}
  .date-tag{background:var(--dark);color:var(--orange);font-family:var(--head);border-radius:4px;padding:2px 7px;line-height:1;white-space:nowrap}
  .intro{color:var(--white);font-weight:600;line-height:1.25}
  .intro strong{color:var(--dark);font-weight:800}
  .pill{background:var(--orange);color:var(--dark);font-weight:800;text-transform:uppercase;border-radius:0 20px 20px 0;padding:3px 14px 3px 8px;font-size:11px;letter-spacing:.3px;white-space:nowrap}
  .pill--dark{background:var(--dark);color:var(--orange);border-radius:20px;padding:4px 14px}

  .services{display:flex}
  .service{display:flex;flex-direction:column;align-items:center;text-align:center;font-size:9px;line-height:1.15;color:var(--white);padding:0 10px;border-right:1px dashed #777}
  .service:last-child{border-right:none}
  .service svg{width:26px;height:22px;margin-bottom:3px}
  .service--on-orange{border-right:none;font-weight:600}

  .contact{color:var(--white);font-size:10px;font-weight:600;line-height:1.6;white-space:nowrap}
  .contact__row{display:flex;align-items:center;gap:5px}
  .contact__icon{width:10px;height:10px;flex:none}
  .contact__gap{width:10px}

  .call-strip{color:var(--white);font-weight:800;font-size:13px;display:flex;align-items:center;gap:8px;white-space:nowrap}
  .call-strip__phone{font-size:15px}

  .photo{position:absolute}
  .address-lines{position:absolute;left:400px;width:150px}
  .address-lines span{display:block;height:1px;background:var(--line);margin-bottom:30px}
  .stamp-box{position:absolute;left:478px;top:20px;width:72px;height:56px;border:1px solid var(--line)}
  .body-copy{color:var(--white);font-size:9.5px;line-height:1.35;font-weight:600}
  .return-address{font-size:7px;color:var(--dark);font-weight:600;white-space:nowrap}
</style>
</head>
<body>

<!-- FRONT -->
<section class="postcard postcard--front">
  <svg class="postcard__shapes" viewBox="0 0 570 380" width="570" height="380">
    <rect width="570" height="380" fill="#f7f7f7"/>
    <rect x="0" y="262" width="570" height="118" fill="#262626"/>
    <path d="M0 150 C90 132 200 130 300 142 L300 285 L0 285 Z" fill="#f0962a"/>
    <path d="M0 348 L330 348 L345 380 L0 380 Z" fill="#f0962a"/>
    <circle cx="410" cy="90" r="186" fill="#ffffff"/>
  </svg>
  <div class="photo" role="img" aria-label="Photo of a yellow backhoe loader parked in a gravel yard under a cloudy sky"
       style="left:235px;top:-85px;width:350px;height:350px;border-radius:50%;background:linear-gradient(180deg,#b9c3cf 0%,#8d96a0 45%,#c9a230 58%,#7a6a58 100%)"></div>

  <div class="abs brand" style="left:22px;top:48px">
    <span class="brand__dot"></span>
    <span class="brand__name">Harlow Auction<br>Service</span>
  </div>

  <h1 class="abs headline" style="left:18px;top:150px;font-size:21px;width:230px">November Online<br>Farm &amp; Construction<br>Machinery Auction</h1>
  <div class="abs date-tag" style="left:18px;top:212px;font-size:16px">November 4th Thru</div>
  <p class="abs intro" style="left:18px;top:236px;font-size:8.5px;width:230px">The 7th Now Accepting Farm and Construction related Items Till <strong>NOVEMBER 1 ST</strong></p>

  <div class="abs pill" style="left:0;top:275px">Auction Services</div>
  <div class="abs services" style="left:8px;top:300px">
    <div class="service">
      <svg viewBox="0 0 26 22" fill="none" stroke="#f0962a" stroke-width="2" stroke-linecap="round"><path d="M4 20 L14 6"/><path d="M10 4 L18 8"/><path d="M22 20 L14 10"/><circle cx="22" cy="18" r="3" fill="#f0962a"/></svg>
      Farm Equipment
    </div>
    <div class="service">
      <svg viewBox="0 0 26 22" fill="none" stroke="#f0962a" stroke-width="2" stroke-linecap="round"><path d="M3 3 L10 13"/><rect x="9" y="11" width="13" height="5" fill="#f0962a"/><circle cx="11" cy="19" r="2.5"/><circle cx="20" cy="19" r="2.5"/></svg>
      Lawn or garden<br>Equipment
    </div>
    <div class="service">
      <svg viewBox="0 0 26 22" fill="none" stroke="#f0962a" stroke-width="2" stroke-linecap="round"><rect x="4" y="8" width="10" height="7" fill="#f0962a"/><path d="M14 10 L20 3 L24 9"/><rect x="3" y="16" width="14" height="4" rx="2"/></svg>
      Vehicle's
    </div>
  </div>

  <div class="abs contact" style="left:320px;top:292px">
    <div class="contact__row"><svg class="contact__icon" viewBox="0 0 10 10"><circle cx="5" cy="4" r="3.5" fill="#f0962a"/><path d="M2 6 L5 10 L8 6Z" fill="#f0962a"/></svg>2210 Meadow Line Rd. Fenwick, MI 48000</div>
    <div class="contact__row"><svg class="contact__icon" viewBox="0 0 10 10"><circle cx="5" cy="5" r="5" fill="#f0962a"/><path d="M3 3 Q3 7 7 7" stroke="#262626" stroke-width="1.4" fill="none"/></svg>MARCUS 555-014-2290</div>
    <div class="contact__row"><svg class="contact__icon" viewBox="0 0 10 10"><circle cx="5" cy="5" r="5" fill="#f0962a"/><path d="M0.5 5 H9.5 M5 0.5 V9.5" stroke="#262626" stroke-width=".8"/></svg>www.harlowauction.com</div>
  </div>

  <div class="abs call-strip" style="left:22px;top:355px">
    CALL US TODAY
    <svg width="14" height="14" viewBox="0 0 14 14"><circle cx="7" cy="7" r="7" fill="#262626"/><path d="M4.5 4 Q4.5 9.5 10 9.5" stroke="#f0962a" stroke-width="1.8" fill="none" stroke-linecap="round"/></svg>
    <span class="call-strip__phone">555-014-7731</span>
  </div>
</section>

<!-- BACK -->
<section class="postcard postcard--back">
  <svg class="postcard__shapes" viewBox="0 0 570 380" width="570" height="380">
    <rect width="570" height="380" fill="#f7f7f7"/>
    <circle cx="160" cy="160" r="228" fill="#f0962a"/>
    <path d="M250 342 L570 342 L570 380 L232 380 Z" fill="#262626"/>
  </svg>
  <div class="photo" role="img" aria-label="Photo of red and white farm tractors and mowers lined up outside a shed"
       style="left:0;top:292px;width:240px;height:88px;background:linear-gradient(180deg,#c6b59a 0%,#b0483a 55%,#8a7f74 100%);border-radius:0 110px 0 0"></div>
  <div class="photo" role="img" aria-label="Photo of an orange hay implement in a gravel lot"
       style="left:300px;top:252px;width:86px;height:86px;border-radius:50%;border:4px solid #ffffff;background:linear-gradient(180deg,#9fc0e0 0%,#c7c1b6 55%,#c4592e 100%)"></div>

  <h2 class="abs headline" style="left:18px;top:28px;font-size:27px;width:360px">November Online Farm and<br><span class="headline__dark">Construction Machinery Auction</span></h2>
  <div class="abs date-tag" style="left:18px;top:88px;font-size:16px;padding:4px 8px">November<br>4th Thru</div>
  <p class="abs intro" style="left:108px;top:90px;font-size:10px;width:240px">The 7th Now Accepting Farm and Construction related Items Till <strong>NOVEMBER 1 ST</strong></p>
  <p class="abs body-copy" style="left:18px;top:136px;width:330px">Harlow Auction Service has been in business for the past Fifty-Five years and defines our success by achieving the highest level of customer satisfaction possible.</p>

  <div class="abs pill pill--dark" style="left:18px;top:190px">Our Product Categories</div>
  <div class="abs services" style="left:14px;top:220px">
    <div class="service service--on-orange">
      <svg viewBox="0 0 26 22" fill="none" stroke="#ffffff" stroke-width="2" stroke-linecap="round"><path d="M4 20 L14 6"/><path d="M10 4 L18 8"/><path d="M22 20 L14 10"/><circle cx="22" cy="18" r="3" fill="#ffffff"/></svg>
      Farm<br>Equipment
    </div>
    <div class="service service--on-orange">
      <svg viewBox="0 0 26 22" fill="none" stroke="#ffffff" stroke-width="2"><rect x="4" y="9" width="8" height="12"/><rect x="14" y="5" width="8" height="16"/><path d="M6 2 H22 M8 2 V9"/></svg>
      Construction<br>Equipment
    </div>
    <div class="service service--on-orange">
      <svg viewBox="0 0 26 22" fill="none" stroke="#ffffff" stroke-width="2" stroke-linecap="round"><path d="M3 3 L10 13"/><rect x="9" y="11" width="13" height="5" fill="#ffffff"/><circle cx="11" cy="19" r="2.5"/><circle cx="20" cy="19" r="2.5"/></svg>
      Lawn or garden<br>Equipment
    </div>
    <div class="service service--on-orange">
      <svg viewBox="0 0 26 22" fill="none" stroke="#ffffff" stroke-width="2" stroke-linecap="round"><rect x="4" y="8" width="10" height="7" fill="#ffffff"/><path d="M14 10 L20 3 L24 9"/><rect x="3" y="16" width="14" height="4" rx="2"/></svg>
      Vehicle's
    </div>
  </div>

  <div class="abs brand" style="left:398px;top:88px">
    <span class="brand__dot" style="width:18px;height:18px"></span>
    <span class="brand__name" style="font-size:16px">Harlow Auction Service</span>
  </div>
  <p class="abs return-address" style="left:398px;top:112px">2210 Meadow Line Rd. Fenwick, MI 48000</p>
  <div class="stamp-box"></div>
  <div class="address-lines" style="top:150px"><span></span><span></span><span></span></div>

  <div class="abs contact" style="left:292px;top:352px;font-size:11px">
    <div class="contact__row"><svg class="contact__icon" viewBox="0 0 10 10"><circle cx="5" cy="5" r="5" fill="#f0962a"/><path d="M3 3 Q3 7 7 7" stroke="#262626" stroke-width="1.4" fill="none"/></svg>555-014-7731<span class="contact__gap"></span><svg class="contact__icon" viewBox="0 0 10 10"><circle cx="5" cy="5" r="5" fill="#f0962a"/><path d="M0.5 5 H9.5 M5 0.5 V9.5" stroke="#262626" stroke-width=".8"/></svg>www.harlowauction.com</div>
  </div>
</section>

</body>
</html>
```